A Real Estate Company Needs a Business Card Design

We need a business card design for a new company based in Boston MA called "Brellmont Real Estate LLC" we are a small company but we like a big corporate look, a simple, sleek, modern and progressive look. we would like the option of having a design that could include the real estate agents personal photo and also a design if the realtor decides not to have a photo. we do not have LOGO at this moment, please use any property look pic corporate with word" Brellmont Real Estate LLC" please see attached file as an example.

```html
<!DOCTYPE html>
<html lang="en">
<head>
<meta charset="utf-8">
<title>Brellmont Real Estate LLC — Business Card</title>
<link rel="stylesheet" href="https://fonts.googleapis.com/css2?family=Open+Sans:wght@400;600;700&display=swap">
<style>
  :root {
    --page-bg: #f2f2f2;
    --card-black: #161616;
    --card-black-soft: #222222;
    --brand-red: #ae1f24;
    --brand-red-dark: #8f171c;
    --text-light: #e6e6e6;
    --text-muted: #bdbdbd;
    --white: #ffffff;
  }
  * { box-sizing: border-box; margin: 0; padding: 0; }
  html, body {
    width: 1200px; height: 800px; overflow: hidden;
    background: var(--page-bg);
    font-family: "Open Sans", Arial, sans-serif;
  }
  .canvas {
    position: relative; width: 1200px; height: 800px;
    display: flex; align-items: center; justify-content: center; gap: 60px;
  }
  .card {
    position: relative; width: 500px; height: 286px;
    border-radius: 18px; overflow: hidden;
    box-shadow: 0 10px 24px rgba(0,0,0,0.22);
  }

  /* Front card */
  .card-front { background: var(--card-black); }
  .front-panel {
    position: absolute; inset: 0 0 auto 0; height: 178px;
    background: linear-gradient(180deg, var(--card-black-soft), var(--card-black));
    border-bottom: 1px solid rgba(255,255,255,0.06);
    box-shadow: 0 6px 14px rgba(0,0,0,0.6);
  }
  .front-brand {
    position: absolute; left: 44px; top: 44px;
    display: flex; flex-direction: column; align-items: flex-start; gap: 16px;
  }
  .brand-square { width: 46px; height: 46px; background: var(--brand-red); }
  .brand-name {
    color: var(--text-light); font-weight: 600; font-size: 17px; letter-spacing: 1px;
  }
  .red-wedge { position: absolute; right: 0; bottom: 0; width: 500px; height: 108px; }
  .contact {
    position: absolute; left: 44px; top: 196px;
    display: grid; grid-template-columns: auto auto; column-gap: 40px; row-gap: 6px;
  }
  .agent-name {
    grid-column: 1 / -1;
    color: var(--brand-red); font-size: 24px; font-weight: 400; letter-spacing: 1px;
  }
  .contact-item {
    display: flex; align-items: center; gap: 8px;
    color: var(--text-muted); font-size: 14px; letter-spacing: 0.5px;
  }
  .contact-item svg { width: 16px; height: 16px; flex: none; }

  /* Back card */
  .card-back {
    background: var(--brand-red);
    display: flex; flex-direction: column; align-items: center; justify-content: center; gap: 22px;
  }
  .back-square { width: 92px; height: 92px; background: var(--white); }
  .back-name {
    color: var(--white); font-weight: 600; font-size: 24px; letter-spacing: 1.5px;
  }
</style>
</head>
<body>
<main class="canvas">
  <section class="card card-front" aria-label="Business card front">
    <div class="front-panel"></div>
    <div class="front-brand">
      <span class="brand-square" aria-hidden="true"></span>
      <span class="brand-name">Brellmont Real Estate LLC</span>
    </div>
    <svg class="red-wedge" viewBox="0 0 500 108" preserveAspectRatio="none" aria-hidden="true">
      <polygon points="330,108 390,0 500,0 500,108" fill="var(--brand-red)"/>
      <polyline points="330,108 390,0" stroke="#9a9a9a" stroke-width="2" fill="none"/>
    </svg>
    <div class="contact">
      <p class="agent-name">Your Name</p>
      <p class="contact-item">
        <svg viewBox="0 0 16 16"><path d="M4 2h2l1 3-1.5 1a8 8 0 0 0 4.5 4.5L11 9l3 1v2a2 2 0 0 1-2 2A10 10 0 0 1 2 4a2 2 0 0 1 2-2z" fill="var(--text-muted)"/></svg>
        000-000-0000
      </p>
      <p class="contact-item">
        <svg viewBox="0 0 16 16"><rect x="1.5" y="3.5" width="13" height="9" fill="none" stroke="var(--text-muted)" stroke-width="1.4"/><polyline points="1.5,3.5 8,9 14.5,3.5" fill="none" stroke="var(--text-muted)" stroke-width="1.4"/></svg>
        email@
      </p>
      <p class="contact-item">
        <svg viewBox="0 0 16 16"><circle cx="8" cy="8" r="6.3" fill="none" stroke="var(--text-muted)" stroke-width="1.3"/><ellipse cx="8" cy="8" rx="2.8" ry="6.3" fill="none" stroke="var(--text-muted)" stroke-width="1.1"/><line x1="1.7" y1="8" x2="14.3" y2="8" stroke="var(--text-muted)" stroke-width="1.1"/></svg>
        website
      </p>
    </div>
  </section>

  <section class="card card-back" aria-label="Business card back">
    <span class="back-square" aria-hidden="true"></span>
    <span class="back-name">Brellmont Real Estate LLC</span>
  </section>
</main>
</body>
</html>
```